New ecommerce website needed for Epoxy Retailer

We need a new shopify website designed and built for our epoxy supply store.
We sell Epoxy, wood, epoxy furniture, supplies and provide classes on how to use epoxy.
We are looking for a website with a home page and 7 primary navigation links at the top. Some of these links should have a drop down menu with the below listed pages linked to them...
Sub Pages:
- Brindle Epoxy
- Epoxy
- Pigments
- Marten Oil
- Molds
- Silicone
- HDPE
- Wood
- Live Edge
- Ovals & Rounds
- Pre-cut
- Charcuterie Wood
- Custom Milling
- Wholesale
- Supplies
- Furniture
-Education
- In person workshops
- My courses (are we able to have a login section for customers to see their purchases?)
- About Us

```html
<!DOCTYPE html>
<html lang="en">
<head>
<meta charset="utf-8">
<title>Timberpour Studio – Epoxy, Wood & Furniture</title>
<link rel="stylesheet" href="https://fonts.googleapis.com/css2?family=Bebas+Neue&family=Montserrat:wght@600;700&family=Dancing+Script:wght@500&family=Arimo:wght@400;700&display=swap">
<style>
:root{
  --red:#e50b0b;
  --ink:#1f1d1e;
  --dark:#2b2829;
  --cream:#f6f3ef;
  --white:#ffffff;
  --grey:#555;
  --line:#e4e0dc;
  --orange:#f05a22;
}
*{margin:0;padding:0;box-sizing:border-box}
html,body{width:1200px;height:4559px;overflow:hidden}
body{position:relative;font-family:"Arimo",Arial,sans-serif;color:var(--ink);background:var(--white)}
.abs{position:absolute}
.display{font-family:"Bebas Neue",Impact,sans-serif;font-weight:400;letter-spacing:.5px}
section{position:absolute;left:0;width:1200px;overflow:hidden}

/* hero */
.hero{top:0;height:620px;background:linear-gradient(180deg,#6d5842 0%,#9a7b55 35%,#7b5a3a 70%,#4a3524 100%)}
.hero-photo{position:absolute;inset:0;background:radial-gradient(ellipse at 70% 40%,rgba(210,200,185,.55),transparent 55%),radial-gradient(ellipse at 20% 80%,rgba(150,95,50,.6),transparent 60%)}
.hero-shade{position:absolute;inset:0;background:rgba(0,0,0,.22)}
.brand{position:absolute;display:flex;align-items:center;gap:8px;color:var(--white);font-family:"Bebas Neue",Impact,sans-serif;font-size:30px;line-height:1;white-space:nowrap}
.brand .dot{width:14px;height:14px;border-radius:50%;background:currentColor}
.nav{position:absolute;left:402px;top:50px;display:flex;gap:30px;font-size:12px;color:var(--white)}
.hero h1{position:absolute;left:0;width:1200px;top:298px;text-align:center;font-family:"Montserrat",sans-serif;font-weight:700;font-size:33px;letter-spacing:1.5px;color:var(--white)}
.hero .tagline{position:absolute;left:0;width:1200px;top:350px;text-align:center;font-family:"Dancing Script",cursive;font-size:31px;color:var(--orange)}
.btn-hero{position:absolute;left:514px;top:420px;width:172px;height:40px;background:var(--orange);color:var(--white);font-size:12px;font-family:"Montserrat",sans-serif;font-weight:600;display:flex;align-items:center;justify-content:center;gap:10px;letter-spacing:.5px}

/* featured */
.featured{top:620px;height:562px;background:var(--cream)}
.section-title{font-family:"Bebas Neue",Impact,sans-serif;font-weight:400;font-size:32px;color:var(--ink)}
.view-all{position:absolute;left:979px;top:80px;font-size:15px;text-decoration:underline;color:var(--ink)}
.product-row{position:absolute;left:161px;top:137px;width:876px;height:333px;background:var(--white);border:1px solid var(--line);display:flex}
.product{flex:1;border-right:1px solid var(--line);position:relative;text-align:center}
.product:last-child{border-right:none}
.shot{position:absolute;left:50%;top:30px;transform:translateX(-50%);width:110px;height:152px;border-radius:10px;background:linear-gradient(180deg,#d8d8d8,#8d9093 60%,#3e4247)}
.name{position:absolute;left:0;right:0;top:203px;font-family:"Bebas Neue",Impact,sans-serif;font-size:17px}
.price{position:absolute;left:0;right:0;top:230px;font-size:16px;color:var(--red)}
.cart-btn{position:absolute;left:50%;top:265px;transform:translateX(-50%);width:128px;height:36px;border:1px solid var(--red);display:flex;align-items:center;background:var(--white);font-size:13px;color:var(--ink)}
.cart-btn .ic{width:34px;height:34px;background:var(--red);display:flex;align-items:center;justify-content:center;margin-right:10px}
.arrow{position:absolute;width:40px;height:40px;border-radius:50%;background:var(--ink);display:flex;align-items:center;justify-content:center}

/* deal */
.deal{top:1182px;height:505px;background:linear-gradient(90deg,#d41414 0%,#e8201a 40%,var(--red) 100%)}
.deal-photo{position:absolute;left:0;top:0;width:560px;height:505px;background:radial-gradient(ellipse at 30% 40%,rgba(255,120,110,.35),transparent 65%)}
.deal h2{position:absolute;left:161px;top:220px;font-size:32px;color:var(--white)}
.deal p{position:absolute;left:163px;top:270px;width:260px;font-size:13px;line-height:23px;color:var(--white)}
.deal-card{position:absolute;left:494px;top:87px;width:543px;height:333px;background:var(--white);display:flex}
.deal-item{flex:1;position:relative;text-align:center;border-right:1px solid var(--line)}
.deal-item:last-child{border-right:none}
.badge{position:absolute;left:8px;top:10px;width:38px;height:38px;border-radius:50%;border:1px solid var(--red);color:var(--red);font-size:10px;line-height:10px;display:flex;flex-direction:column;align-items:center;justify-content:center}
.deal-item .name{top:205px}
.deal-item .price{top:233px}
.deal-item .price s{color:var(--grey);font-size:13px;margin-right:8px}

/* reviews */
.reviews{top:1687px;height:552px;background:var(--cream)}
.reviews .section-title{position:absolute;left:0;width:1200px;text-align:center;top:88px}
.review{position:absolute;top:155px;width:584px;height:263px;background:var(--white);text-align:center}
.review .avatar{position:absolute;left:50%;top:39px;transform:translateX(-50%);width:62px;height:62px;border-radius:50%;border:2px solid var(--orange);background:#f2d7b8}
.review p{position:absolute;left:40px;right:40px;top:107px;font-size:13px;line-height:23px;color:var(--ink)}
.review .who{position:absolute;left:0;right:0;top:207px;font-family:"Bebas Neue",Impact,sans-serif;font-size:18px;color:var(--red)}
.quote-mark{position:absolute;right:30px;font-family:Georgia,serif;font-size:160px;color:rgba(229,11,11,.08);top:40px;line-height:1}
.dots{position:absolute;left:549px;top:448px;display:flex;gap:6px}
.dots span{width:12px;height:12px;border:1px solid #aaa}
.dots span.on{background:var(--red);border-color:var(--red)}

/* how to */
.howto{top:2239px;height:713px;background:linear-gradient(180deg,#262324,#3a3637 60%,#2f2b2c)}
.howto .section-title{position:absolute;left:0;width:1200px;text-align:center;top:82px;color:var(--red)}
.howto .lead{position:absolute;left:290px;width:620px;top:158px;text-align:center;font-size:13px;line-height:23px;color:var(--white)}
.tip{position:absolute;width:240px;color:var(--white)}
.tip svg{display:block;margin-bottom:12px}
.tip h3{font-family:"Bebas Neue",Impact,sans-serif;font-size:21px;color:var(--red);font-weight:400}
.tip p{font-size:13px;line-height:22px;margin-top:4px}
.worker{position:absolute;left:442px;top:221px;width:381px;height:398px;border-radius:40% 40% 10% 10%;background:linear-gradient(180deg,#c4a58b 0%,#d9d9d9 30%,#3d5b8a 65%,#2c4670 100%);opacity:.85}
.btn-red{position:absolute;width:134px;height:44px;background:var(--red);color:var(--white);font-size:16px;display:flex;align-items:center;justify-content:center}

/* about */
.about{top:2952px;height:791px;background:linear-gradient(180deg,#ffffff 0%,#f3f3f3 55%,#dcdcdc 100%)}
.about .mist{position:absolute;left:0;top:300px;width:1200px;height:491px;background:radial-gradient(ellipse at 20% 70%,rgba(150,150,150,.35),transparent 60%),radial-gradient(ellipse at 85% 60%,rgba(160,160,160,.3),transparent 55%)}
.about .section-title{position:absolute;left:0;width:1200px;text-align:center;top:150px}
.about .copy{position:absolute;left:215px;width:770px;text-align:center;font-size:13px;line-height:23px;color:var(--ink)}
.perk{position:absolute;top:581px;width:280px;height:119px;background:var(--white);display:flex;align-items:center;padding-left:18px;gap:14px}
.perk h4{font-family:"Bebas Neue",Impact,sans-serif;font-size:20px;font-weight:400}
.perk p{font-size:13px;line-height:22px;color:var(--ink)}

/* newsletter + contact */
.signup{top:3743px;height:378px;background:var(--red);color:var(--white)}
.signup .divider{position:absolute;left:600px;top:0;width:1px;height:378px;background:rgba(255,255,255,.7)}
.signup h2{position:absolute;top:106px;font-size:32px;color:var(--white)}
.signup .sub{position:absolute;left:161px;top:154px;font-size:13px}
.email-field{position:absolute;left:161px;top:199px;width:330px;height:43px;background:var(--white);color:var(--ink);font-size:13px;display:flex;align-items:center;gap:10px;padding-left:12px}
.subscribe{position:absolute;left:161px;top:261px;width:119px;height:42px;background:var(--ink);color:var(--white);font-size:15px;display:flex;align-items:center;justify-content:center}
.contact-row{position:absolute;left:708px;display:flex;gap:20px;font-size:13px;line-height:20px}
.contact-row .ic{width:39px;height:39px;border:1px solid var(--white);display:flex;align-items:center;justify-content:center;flex:none}

/* footer */
.footer{top:4121px;height:389px;background:var(--cream)}
.footer h5{position:absolute;top:92px;font-family:"Bebas Neue",Impact,sans-serif;font-weight:400;font-size:21px}
.footer ul{position:absolute;top:135px;list-style:none;font-size:13px;line-height:28px}
.social li{display:flex;align-items:center;gap:8px;line-height:38px}
.social .pip{width:27px;height:27px;border-radius:50%;border:1px solid var(--red);display:inline-block}
.footer .brand{color:var(--ink);left:872px;top:150px;font-size:40px}
.copyright{position:absolute;left:0;top:4510px;width:1200px;height:49px;background:var(--dark);color:var(--white);font-size:13px;display:flex;align-items:center;justify-content:center}
</style>
</head>
<body>

<section class="hero">
  <div class="hero-photo" role="img" aria-label="Bright kitchen interior with wooden floor, granite counter and stainless fridge"></div>
  <div class="hero-shade"></div>
  <div class="brand" style="left:162px;top:57px"><span class="dot"></span>Timberpour Studio</div>
  <nav class="nav">
    <span>Home</span><span>About Us</span><span>Service</span><span>Wholesale</span><span>Supplies</span><span>Furniture</span><span>Education</span><span>Contact Us</span>
  </nav>
  <h1>WE SELL EPOXY, WOOD, EPOXY FURNITURE</h1>
  <div class="tagline">Supplies And Provide Classes On How To Use Epoxy</div>
  <a class="btn-hero">CONTENT US
    <svg width="40" height="8" viewBox="0 0 40 8"><path d="M0 4h37M33 1l4 3-4 3" stroke="#fff" fill="none" stroke-width="1.2"/></svg></a>
</section>

<section class="featured">
  <h2 class="section-title abs" style="left:161px;top:71px">Featured Products</h2>
  <span class="view-all">View All</span>
  <div class="product-row">
    <div class="product">
      <div class="shot" style="background:linear-gradient(90deg,#e6e6e6 0 45%,#f0c419 45%)" role="img" aria-label="Two bottles of Marten Oil"></div>
      <div class="name">Marten Oil</div><div class="price">$250.00</div>
      <div class="cart-btn"><span class="ic"><svg width="16" height="16" viewBox="0 0 16 16"><path d="M1 2h2l2 8h8l2-6H4" stroke="#fff" fill="none" stroke-width="1.5"/><circle cx="6" cy="13" r="1.3" fill="#fff"/><circle cx="12" cy="13" r="1.3" fill="#fff"/></svg></span>Add To Cart</div>
    </div>
    <div class="product">
      <div class="shot" style="background:linear-gradient(180deg,#f2f2f2,#d4d4d4)" role="img" aria-label="White jug of pigments"></div>
      <div class="name">Pigments</div><div class="price">$1205.99</div>
      <div class="cart-btn"><span class="ic"><svg width="16" height="16" viewBox="0 0 16 16"><path d="M1 2h2l2 8h8l2-6H4" stroke="#fff" fill="none" stroke-width="1.5"/><circle cx="6" cy="13" r="1.3" fill="#fff"/><circle cx="12" cy="13" r="1.3" fill="#fff"/></svg></span>Add To Cart</div>
    </div>
    <div class="product">
      <div class="shot" role="img" aria-label="Grey bottle of Brindle Epoxy"></div>
      <div class="name">Brindle Epoxy</div><div class="price">$145.99</div>
      <div class="cart-btn"><span class="ic"><svg width="16" height="16" viewBox="0 0 16 16"><path d="M1 2h2l2 8h8l2-6H4" stroke="#fff" fill="none" stroke-width="1.5"/><circle cx="6" cy="13" r="1.3" fill="#fff"/><circle cx="12" cy="13" r="1.3" fill="#fff"/></svg></span>Add To Cart</div>
    </div>
    <div class="product">
      <div class="shot" role="img" aria-label="Two jugs of charcuterie wood finish"></div>
      <div class="name">Charcuterie Wood</div><div class="price">$2250.00</div>
      <div class="cart-btn"><span class="ic"><svg width="16" height="16" viewBox="0 0 16 16"><path d="M1 2h2l2 8h8l2-6H4" stroke="#fff" fill="none" stroke-width="1.5"/><circle cx="6" cy="13" r="1.3" fill="#fff"/><circle cx="12" cy="13" r="1.3" fill="#fff"/></svg></span>Add To Cart</div>
    </div>
  </div>
  <div class="arrow" style="left:141px;top:284px"><svg width="10" height="10"><path d="M7 1L2 5l5 4z" fill="#fff"/></svg></div>
  <div class="arrow" style="left:1017px;top:284px"><svg width="10" height="10"><path d="M3 1l5 4-5 4z" fill="#fff"/></svg></div>
</section>

<section class="deal">
  <div class="deal-photo" role="img" aria-label="Hands working poured epoxy, red-tinted"></div>
  <svg class="abs" style="left:161px;top:178px" width="60" height="30" viewBox="0 0 60 30"><path d="M2 28L20 8l8 8 8-12 22 24z" fill="none" stroke="#fff" stroke-width="2"/><path d="M2 28h56" stroke="#fff" stroke-width="2"/></svg>
  <h2 class="display">Deal Of The Day</h2>
  <p>Lorem ipsum dolor sit amet, consectetuer adipiscing elit, sed diam nonummy nibh euismod tincidunt ut.</p>
  <div class="deal-card">
    <div class="deal-item">
      <div class="badge">25%<span>OFF</span></div>
      <div class="shot" role="img" aria-label="Grey bottle of Brindle Epoxy"></div>
      <div class="name">Brindle Epoxy</div>
      <div class="price"><s>$1450.00</s>$1087.50</div>
      <div class="cart-btn"><span class="ic"><svg width="16" height="16" viewBox="0 0 16 16"><path d="M1 2h2l2 8h8l2-6H4" stroke="#fff" fill="none" stroke-width="1.5"/><circle cx="6" cy="13" r="1.3" fill="#fff"/><circle cx="12" cy="13" r="1.3" fill="#fff"/></svg></span>Add To Cart</div>
    </div>
    <div class="deal-item">
      <div class="badge">15%<span>OFF</span></div>
      <div class="shot" role="img" aria-label="Two jugs of charcuterie wood finish"></div>
      <div class="name">Charcuterie Wood</div>
      <div class="price"><s>$2250.00</s>$1912.50</div>
      <div class="cart-btn"><span class="ic"><svg width="16" height="16" viewBox="0 0 16 16"><path d="M1 2h2l2 8h8l2-6H4" stroke="#fff" fill="none" stroke-width="1.5"/><circle cx="6" cy="13" r="1.3" fill="#fff"/><circle cx="12" cy="13" r="1.3" fill="#fff"/></svg></span>Add To Cart</div>
    </div>
  </div>
  <div class="arrow" style="left:474px;top:233px"><svg width="10" height="10"><path d="M7 1L2 5l5 4z" fill="#fff"/></svg></div>
  <div class="arrow" style="left:1017px;top:233px"><svg width="10" height="10"><path d="M3 1l5 4-5 4z" fill="#fff"/></svg></div>
</section>

<section class="reviews">
  <h2 class="section-title">Customer Reviews</h2>
  <div class="review" style="left:-306px">
    <span class="quote-mark">&ldquo;</span>
    <div class="avatar" role="img" aria-label="Customer portrait"></div>
    <p>Lorem ipsum dolor sit amet, consectetuer adipiscing elit, sed diam nonummy nibh euismod tincidunt ut laoreet dolore magna aliquam erat volutpat. Ut wisi enim ad minim veniam, quis nostrud exerci tation ullamcorper suscipit lobortis nisl ut aliquip ex ea commodo consequat.</p>
    <div class="who">Rowan William</div>
  </div>
  <div class="review" style="left:308px">
    <span class="quote-mark">&ldquo;</span>
    <div class="avatar" role="img" aria-label="Customer portrait"></div>
    <p>Lorem ipsum dolor sit amet, consectetuer adipiscing elit, sed diam nonummy nibh euismod tincidunt ut laoreet dolore magna aliquam erat volutpat. Ut wisi enim ad minim veniam, quis nostrud exerci tation ullamcorper suscipit lobortis nisl ut aliquip ex ea commodo consequat.</p>
    <div class="who">Delia Harrow</div>
  </div>
  <div class="review" style="left:922px">
    <div class="avatar" role="img" aria-label="Customer portrait"></div>
    <p>Lorem ipsum dolor sit amet, consectetuer adipiscing elit, sed diam nonummy nibh euismod tincidunt ut laoreet dolore magna aliquam erat volutpat. Ut wisi enim ad minim veniam, quis nostrud exerci tation ullamcorper suscipit lobortis nisl ut aliquip ex ea commodo consequat.</p>
    <div class="who">Benzel Ford</div>
  </div>
  <div class="dots"><span></span><span></span><span class="on"></span><span></span><span></span><span></span></div>
</section>

<section class="howto">
  <h2 class="section-title">How To Use Epoxy</h2>
  <p class="lead">Lorem ipsum dolor sit amet, consectetuer adipiscing elit, sed diam nonummy nibh euismod tincidunt ut laoreet dolore magna aliquam erat volutpat.</p>
  <div class="worker" role="img" aria-label="Worker spreading epoxy on a warehouse floor with a long roller"></div>
  <div class="tip" style="left:165px;top:210px">
    <svg width="52" height="48" viewBox="0 0 52 48" fill="none" stroke="#fff" stroke-width="2"><path d="M6 44l6-22h28l6 22zM9 33h34M26 22v22"/><path d="M10 4v8M6 8h8M24 2v6M21 5h6"/></svg>
    <h3>Lorem Ipsum</h3><p>Lorem ipsum dolor sit amet consectetuer adipiscing elit sed .</p>
  </div>
  <div class="tip" style="left:165px;top:392px">
    <svg width="52" height="48" viewBox="0 0 52 48" fill="none" stroke="#fff" stroke-width="2"><path d="M30 4l12 6-6 12-12-6zM28 20c-4 4-8 8-10 14"/><path d="M2 38c6-4 10 4 16 0s10 4 16 0 10 4 16 0M2 45c6-4 10 4 16 0s10 4 16 0 10 4 16 0"/></svg>
    <h3>Lorem Ipsum</h3><p>Lorem ipsum dolor sit amet consectetuer adipiscing elit sed .</p>
  </div>
  <div class="tip" style="left:830px;top:210px">
    <svg width="52" height="48" viewBox="0 0 52 48" fill="none" stroke="#fff" stroke-width="2"><path d="M44 4L20 38M14 36h14l-4 8H10zM4 46h44"/></svg>
    <h3>Lorem Ipsum</h3><p>Lorem ipsum dolor sit amet consectetuer adipiscing elit sed .</p>
  </div>
  <div class="tip" style="left:830px;top:392px">
    <svg width="52" height="48" viewBox="0 0 52 48" fill="none" stroke="#fff" stroke-width="2"><circle cx="34" cy="18" r="12"/><circle cx="34" cy="18" r="5"/><path d="M2 14h16M6 22h14M2 30h18M10 38h26"/></svg>
    <h3>Lorem Ipsum</h3><p>Lorem ipsum dolor sit amet consectetuer adipiscing elit sed .</p>
  </div>
  <a class="btn-red" style="left:533px;top:634px">Contact Us</a>
</section>

<section class="about">
  <div class="mist" role="img" aria-label="Misty pine forest"></div>
  <h2 class="section-title">About Timberpour</h2>
  <p class="copy" style="top:222px">Lorem ipsum dolor sit amet, consectetuer adipiscing elit, sed diam nonummy nibh euismod tincidunt ut laoreet dolore magna aliquam erat volutpat. Ut wisi enim ad minim veniam, quis nostrud exerci tation ullamcorper suscipit lobortis nisl ut aliquip ex ea commodo consequat.</p>
  <p class="copy" style="top:297px">Lorem ipsum dolor sit amet, consectetuer adipiscing elit, sed diam nonummy nibh euismod tincidunt ut laoreet dolore magna aliquam erat volutpat. Ut wisi enim ad minim veniam, quis nostrud exerci tation ullamcorper suscipit lobortis nisl ut aliquip ex ea commodo consequat.</p>
  <a class="btn-red" style="left:533px;top:377px">Read More</a>
  <div class="perk" style="left:161px">
    <svg width="58" height="44" viewBox="0 0 58 44" fill="none" stroke="#e50b0b" stroke-width="2"><path d="M12 6h26v26H12zM38 14h10l8 10v8H38M2 12h8M4 20h8M2 28h8"/><circle cx="20" cy="36" r="5"/><circle cx="46" cy="36" r="5"/></svg>
    <div><h4>Free Delivery</h4><p>Lorem ipsu dot amet tuer<br>adip consectetuer.</p></div>
  </div>
  <div class="perk" style="left:460px">
    <svg width="50" height="44" viewBox="0 0 50 44" fill="none" stroke="#e50b0b" stroke-width="2"><rect x="2" y="4" width="38" height="26" rx="2"/><path d="M2 12h38M8 22h12"/><rect x="32" y="26" width="14" height="14"/><path d="M35 26v-4a4 4 0 018 0v4"/></svg>
    <div><h4>Secure Payment</h4><p>Lorem ilor sit amet tuer<br>adip consectetuer.</p></div>
  </div>
  <div class="perk" style="left:759px">
    <svg width="48" height="46" viewBox="0 0 48 46" fill="none" stroke="#e50b0b" stroke-width="2"><path d="M10 6l8 10-5 5c3 6 7 10 13 13l5-5 10 8-6 6C20 42 6 28 4 12z"/><circle cx="32" cy="16" r="12"/><text x="25" y="20" font-size="10" fill="#e50b0b" stroke="none" font-family="Arial">24</text></svg>
    <div><h4>Help &amp; Support</h4><p>Lorem ipsu dol amet tuer<br>adip consectetuer.</p></div>
  </div>
</section>

<section class="signup">
  <div class="divider"></div>
  <h2 class="display" style="left:161px">Newsletter Sign Up</h2>
  <p class="sub">To Get Latest Updates SUBSCRIBE Our Newsletter.</p>
  <div class="email-field"><svg width="14" height="10" viewBox="0 0 14 10"><rect width="14" height="10" fill="#1f1d1e"/><path d="M0 0l7 6 7-6" stroke="#fff" fill="none"/></svg>Enter email id</div>
  <div class="subscribe">Subscribe</div>
  <h2 class="display" style="left:708px">Contact Details</h2>
  <div class="contact-row" style="top:164px">
    <span class="ic"><svg width="14" height="18" viewBox="0 0 14 18"><path d="M7 17s6-6 6-10A6 6 0 001 7c0 4 6 10 6 10z" fill="none" stroke="#fff" stroke-width="1.5"/><circle cx="7" cy="7" r="2" fill="#fff"/></svg></span>
    <span>123, Building Name, Street<br>City, State XY 123456</span>
  </div>
  <div class="contact-row" style="top:214px">
    <span class="ic"><svg width="16" height="16" viewBox="0 0 16 16"><path d="M3 1l3 4-2 2c1 2 3 4 5 5l2-2 4 3-2 2C7 15 1 9 1 3z" fill="none" stroke="#fff" stroke-width="1.4"/></svg></span>
    <span>Phone Us<br>+1 555 014 2286</span>
  </div>
  <div class="contact-row" style="top:264px">
    <span class="ic"><svg width="16" height="12" viewBox="0 0 16 12"><rect x=".7" y=".7" width="14.6" height="10.6" fill="none" stroke="#fff" stroke-width="1.4"/><path d="M1 1l7 6 7-6" stroke="#fff" fill="none" stroke-width="1.4"/></svg></span>
    <span>Email Us<br>info@timberpourstudio.com</span>
  </div>
</section>

<section class="footer">
  <h5 style="left:163px">Quick Links</h5>
  <ul style="left:163px"><li>Home</li><li>Products</li><li>Wholsale</li><li>Supplies</li><li>Furniture</li><li>Education</li><li>About Us</li><li>Contact Us</li></ul>
  <h5 style="left:379px">My Account</h5>
  <ul style="left:379px"><li>Your Account</li><li>FAQs</li><li>Terms &amp; Conditions</li><li>Return Policy</li><li>Shipping Info</li><li>Privacy Policy</li><li>Cookies</li></ul>
  <h5 style="left:637px">Social Media</h5>
  <ul class="social" style="left:637px;top:132px"><li><span class="pip"></span>Chatterly</li><li><span class="pip"></span>Flitter</li><li><span class="pip"></span>ReelHub</li><li><span class="pip"></span>WorkLink</li><li><span class="pip"></span>Snapwall</li></ul>
  <div class="brand"><span class="dot"></span>Timberpour</div>
</section>

<div class="copyright">© 2023 Timberpour Studio. All Rights Reserved.</div>

</body>
</html>
```